Vorna Fleet business card

I am needing a business card that at a glance shows all the services that we provide emphasizing some more than others. We are a Fleet and Compliance management company as well as a software company. We provide outsourced solutions for KPX compliance and HR services via our own software.
In addition, we do
drug testing
GPS
Cameras
Electronic DVIRS
ELD's

Target Market(s)

Transportation company owners

Industry/Entity Type

Transportation supplier

Contact Information for Business Card

the card should inform potential customers what we do

Other font styles liked:
• I have added brand guidelines. See attached

Requirements
Must have
• See description
Should not have
• Colors outside my brand guide. See attached

```html
<!DOCTYPE html>
<html lang="en">
<head>
<meta charset="utf-8">
<title>Vorna Fleet business card</title>
<link href="https://fonts.googleapis.com/css2?family=Montserrat:wght@400;700;800&family=Questrial&display=swap" rel="stylesheet">
<style>
  :root {
    --brand-red: #ee2b32;
    --ink: #070809;
    --paper: #ffffff;
    --stage: #2a2a2a;
    --rule: #1b1b1b;
  }
  * { box-sizing: border-box; margin: 0; padding: 0; }
  html, body { width: 1200px; height: 895px; overflow: hidden; }
  body {
    background: var(--stage);
    display: flex;
    align-items: center;
    justify-content: center;
    gap: 40px;
    font-family: "Questrial", "Montserrat", sans-serif;
  }
  .card {
    position: relative;
    width: 540px;
    height: 310px;
    overflow: hidden;
    box-shadow: 0 12px 30px rgba(0,0,0,.5);
  }

  /* Front: services */
  .card-front { background: var(--ink); color: var(--paper); }
  .front-wordmark {
    position: absolute;
    top: 58px; left: 0; right: 0;
    display: flex; align-items: center; justify-content: center; gap: 14px;
    font-family: "Montserrat", sans-serif;
    font-weight: 800;
    font-size: 44px;
    letter-spacing: 3px;
    color: var(--paper);
  }
  .front-wordmark .mark-square { width: 30px; height: 30px; background: var(--brand-red); }
  .services {
    position: absolute;
    left: 26px; right: 26px; bottom: 48px;
    display: flex; justify-content: space-between; align-items: flex-end;
    list-style: none;
  }
  .service {
    display: flex; flex-direction: column; align-items: center; gap: 8px;
    font-size: 12px; letter-spacing: .3px;
    white-space: nowrap; text-align: center;
  }
  .service svg { width: 30px; height: 30px; fill: none; stroke: var(--brand-red); stroke-width: 1.4; stroke-linecap: round; stroke-linejoin: round; }
  .front-band {
    position: absolute;
    left: 0; right: 0; bottom: 12px;
    height: 16px;
    background: var(--brand-red);
  }

  /* Back: contact */
  .card-back { background: var(--paper); color: var(--ink); }
  .back-wordmark {
    position: absolute;
    left: 36px; top: 138px;
    display: flex; align-items: center; gap: 10px;
    font-family: "Montserrat", sans-serif;
    font-weight: 800;
    font-size: 26px;
    letter-spacing: .5px;
    color: var(--ink);
    white-space: nowrap;
  }
  .back-wordmark .mark-square { width: 20px; height: 20px; background: var(--brand-red); }
  .divider {
    position: absolute;
    left: 284px; top: 92px;
    width: 1px; height: 126px;
    background: var(--rule);
  }
  .contact { position: absolute; left: 304px; top: 92px; }
  .person-name {
    font-family: "Montserrat", sans-serif;
    font-weight: 800;
    font-size: 19px;
    color: var(--brand-red);
    letter-spacing: .3px;
  }
  .person-role { font-size: 14px; margin-top: 2px; margin-bottom: 10px; }
  .contact-list { list-style: none; }
  .contact-list li {
    display: flex; align-items: center; gap: 8px;
    font-size: 13.5px; line-height: 20px; letter-spacing: .3px;
    white-space: nowrap;
  }
  .contact-list svg { width: 11px; height: 11px; fill: var(--brand-red); flex: none; }
</style>
</head>
<body>

  <section class="card card-front" aria-label="Card front">
    <div class="front-wordmark"><span class="mark-square"></span>Vorna Fleet</div>

    <ul class="services">
      <li class="service">
        <svg viewBox="0 0 30 30"><rect x="6" y="4" width="8" height="3"/><path d="M7 7v15a3 3 0 0 0 6 0V7"/><path d="M7 14h6"/><circle cx="21" cy="20" r="4"/><path d="M18 23l6-6"/></svg>
        Drug Testing
      </li>
      <li class="service">
        <svg viewBox="0 0 30 30"><path d="M15 24s-7-7-7-12a7 7 0 0 1 14 0c0 5-7 12-7 12z"/><circle cx="15" cy="12" r="2.5"/><ellipse cx="15" cy="25" rx="8" ry="2"/></svg>
        GPS
      </li>
      <li class="service">
        <svg viewBox="0 0 30 30"><rect x="3" y="9" width="24" height="15" rx="2"/><path d="M10 9l2-3h6l2 3"/><circle cx="15" cy="16.5" r="4.5"/><circle cx="15" cy="16.5" r="2"/><path d="M15 1v2M10 2l1 2M20 2l-1 2"/></svg>
        Cameras
      </li>
      <li class="service">
        <svg viewBox="0 0 30 30"><rect x="9" y="9" width="12" height="12"/><rect x="12" y="12" width="6" height="6"/><path d="M12 9V4M15 9V3M18 9V4M12 21v5M15 21v6M18 21v5M9 12H4M9 15H3M9 18H4M21 12h5M21 15h6M21 18h5"/></svg>
        Electronic DVIRS
      </li>
      <li class="service">
        <svg viewBox="0 0 30 30"><rect x="9" y="3" width="12" height="5"/><rect x="9" y="22" width="12" height="5"/><rect x="7" y="8" width="16" height="14" rx="3"/><circle cx="15" cy="15" r="4"/><path d="M15 13v2l1.5 1"/></svg>
        ELD's
      </li>
    </ul>

    <div class="front-band"></div>
  </section>

  <section class="card card-back" aria-label="Card back">
    <div class="back-wordmark"><span class="mark-square"></span>Vorna Fleet</div>
    <div class="divider"></div>
    <div class="contact">
      <p class="person-name">MARCUS HALE</p>
      <p class="person-role">Founder and CEO</p>
      <ul class="contact-list">
        <li><svg viewBox="0 0 12 12"><path d="M2.5 1l2 2.5-1 1.2a7 7 0 0 0 3.8 3.8l1.2-1 2.5 2-1.2 1.5C5.5 11 1 6.5 1 2.2z"/></svg>000 000 0000</li>
        <li><svg viewBox="0 0 12 12"><rect x="3" y="1" width="6" height="3"/><rect x="1" y="4" width="10" height="5" rx="1"/><rect x="3" y="8" width="6" height="3"/></svg>000 000 0000</li>
        <li><svg viewBox="0 0 12 12"><path d="M1 2h10v8H1z M1.8 2.8L6 6.5l4.2-3.7" fill="none" stroke="#ee2b32" stroke-width="1.4"/></svg>info@vornafleet.com.au</li>
        <li><svg viewBox="0 0 12 12"><circle cx="6" cy="6" r="5" fill="none" stroke="#ee2b32" stroke-width="1.2"/><path d="M1 6h10M6 1c-2.5 3-2.5 7 0 10M6 1c2.5 3 2.5 7 0 10" fill="none" stroke="#ee2b32" stroke-width="1"/></svg>www.vornafleet.com.au</li>
      </ul>
    </div>
  </section>

</body>
</html>
```